Butcher shop

We have 2 butcher shops:

Shop 9, Ridgeway Court, Aberdeen NSW 2336
Ph 02 6512 3840

47 Marlow St, Scone NSW 2337
Ph 02 6518 2274

ABN 48 907 215 816

I would like this info on reverse of card and my personal info on front of card. I have a logo I would like to use also. Require a very smooth thick matte card, with colour both sides.

Front of card should say:

Linda Farrugia
Accounts

Ph 0437 620 915
E lindafarrugia@quollmail.com.au

Industry/Entity Type

Shop

Contact Information for Business Card

Linda Farrugia
Ph 0437 620 915

Logo Text

Farrugia's Quality Meats

Logo styles of interest
Pictorial/Combination Logo
Requirements
Must have
• We use Century Gothic Font

```html
<!DOCTYPE html>
<html lang="en">
<head>
<meta charset="utf-8">
<title>Butcher Shop Business Card – Reverse</title>
<link rel="stylesheet" href="https://fonts.googleapis.com/css2?family=Questrial&display=swap">
<style>
  :root {
    --paper: #ffffff;
    --sky: #84d2f0;
    --tint-on-paper: #e4f3fb;
    --tint-on-sky: #a2dcf4;
    --ink: #111111;
  }
  html, body {
    margin: 0;
    padding: 0;
    width: 1200px;
    height: 692px;
    overflow: hidden;
    background: var(--paper);
  }
  .card {
    position: relative;
    width: 1200px;
    height: 692px;
    overflow: hidden;
    font-family: "Questrial", "Century Gothic", sans-serif;
    color: var(--ink);
  }
  .half {
    position: absolute;
    top: 0;
    height: 100%;
  }
  .half--aberdeen { left: 0; width: 600px; background: var(--paper); }
  .half--scone { left: 600px; width: 600px; background: var(--sky); }

  .motif {
    position: absolute;
    top: 110px;
    height: 582px;
  }
  .motif--paper {
    left: 0;
    width: 520px;
    background: var(--tint-on-paper);
    border-top-right-radius: 200px;
  }
  .motif--sky {
    left: 690px;
    width: 510px;
    background: var(--tint-on-sky);
    border-top-left-radius: 200px;
  }

  .shop {
    position: absolute;
    top: 224px;
    width: 600px;
    margin: 0;
    text-align: center;
    font-size: 47px;
    line-height: 56px;
    font-style: normal;
  }
  .shop--aberdeen { left: 0; }
  .shop--scone { left: 600px; }
  .shop__line { display: block; white-space: nowrap; }
  .shop__phone {
    display: inline-flex;
    align-items: center;
    gap: 8px;
  }
  .phone-icon {
    width: 34px;
    height: 34px;
  }

  .abn {
    position: absolute;
    left: 0;
    width: 1200px;
    top: 604px;
    margin: 0;
    text-align: center;
    font-size: 39px;
    line-height: 44px;
  }
</style>
</head>
<body>
<div class="card">
  <div class="half half--aberdeen"></div>
  <div class="half half--scone"></div>

  <div class="motif motif--paper" role="img" aria-label="Faint large cow silhouette decoration"></div>
  <div class="motif motif--sky" role="img" aria-label="Faint large cow silhouette decoration"></div>

  <address class="shop shop--aberdeen">
    <span class="shop__line">Shop 9, Ridgeway Court</span>
    <span class="shop__line">Aberdeen NSW 2336</span>
    <span class="shop__line shop__phone">
      <svg class="phone-icon" viewBox="0 0 34 34" aria-hidden="true">
        <circle cx="17" cy="17" r="15" fill="none" stroke="currentColor" stroke-width="2.6"/>
        <path d="M12 8 h5 v6 h-3 q-1 3 0 6 h3 v6 h-5 q-5 -9 0 -18z" fill="currentColor"/>
      </svg>
      02 6512 3840
    </span>
  </address>

  <address class="shop shop--scone">
    <span class="shop__line">47 Marlow St</span>
    <span class="shop__line">Scone NSW 2337</span>
    <span class="shop__line shop__phone">
      <svg class="phone-icon" viewBox="0 0 34 34" aria-hidden="true">
        <circle cx="17" cy="17" r="15" fill="none" stroke="currentColor" stroke-width="2.6"/>
        <path d="M12 8 h5 v6 h-3 q-1 3 0 6 h3 v6 h-5 q-5 -9 0 -18z" fill="currentColor"/>
      </svg>
      02 6518 2274
    </span>
  </address>

  <p class="abn">ABN 48 907 215 816</p>
</div>
</body>
</html>
```